Inspiration Poster

Inspirational Poster that has a Kamran Dulo like abstract look (http://www.vexalo.com/images/search?q=kamran+dulo&FORM=HDRSC2) with the text:

"we walk not in order to arrive at the promise land but because walking itself is a revolution"
-Peter Ambrick

```html
<!DOCTYPE html>
<html lang="en">
<head>
<meta charset="utf-8">
<title>Inspiration Poster – Peter Ambrick</title>
<link rel="stylesheet" href="https://fonts.googleapis.com/css2?family=Open+Sans:wght@400&family=Cinzel:wght@700&display=swap">
<style>
  :root {
    --quote-red: #e3131b;
    --halo: rgba(190, 235, 255, 0.95);
    --halo-soft: rgba(255, 255, 255, 0.6);
    --author-white: #ffffff;
    --author-edge: #14202e;
    --bokeh-yellow: #f2e23a;
    --bokeh-green: #4aa84a;
    --bokeh-light: #fdfbe0;
    --bokeh-cyan: #1fa8e6;
    --bokeh-blue: #0b63b6;
    --bokeh-deep: #0a2f5a;
  }
  html, body {
    margin: 0;
    padding: 0;
    width: 900px;
    height: 1200px;
    overflow: hidden;
    background: var(--bokeh-deep);
  }
  .poster {
    position: relative;
    width: 900px;
    height: 1200px;
    overflow: hidden;
  }
  .poster__backdrop {
    position: absolute;
    inset: 0;
    background:
      radial-gradient(ellipse 260px 220px at 340px 640px, var(--bokeh-light) 0%, rgba(253,251,224,0) 100%),
      radial-gradient(ellipse 420px 360px at 330px 280px, var(--bokeh-yellow) 0%, rgba(242,226,58,0) 100%),
      radial-gradient(ellipse 380px 520px at 0px 300px, var(--bokeh-green) 0%, rgba(74,168,74,0) 100%),
      radial-gradient(ellipse 700px 700px at 520px 620px, var(--bokeh-cyan) 0%, rgba(31,168,230,0) 100%),
      linear-gradient(180deg, #1c4f6e 0%, var(--bokeh-blue) 55%, var(--bokeh-deep) 100%);
  }
  .quote {
    position: absolute;
    left: 118px;
    top: 268px;
    margin: 0;
    font-family: "Open Sans", "Segoe UI", sans-serif;
    font-weight: 400;
    font-size: 73px;
    line-height: 104px;
    letter-spacing: -0.5px;
    color: var(--quote-red);
    text-shadow:
      0 0 3px var(--halo),
      0 0 6px var(--halo),
      0 0 10px var(--halo-soft),
      0 0 14px var(--halo-soft);
  }
  .quote__line { display: block; white-space: nowrap; }
  .author {
    position: absolute;
    right: 72px;
    top: 992px;
    margin: 0;
    font-family: "Cinzel", "Times New Roman", serif;
    font-weight: 700;
    font-size: 30px;
    letter-spacing: 1px;
    color: var(--author-white);
    text-shadow:
      -1px -1px 0 var(--author-edge), 1px -1px 0 var(--author-edge),
      -1px 1px 0 var(--author-edge), 1px 1px 0 var(--author-edge),
      0 2px 3px rgba(0,0,0,0.6);
  }
</style>
</head>
<body>
  <main class="poster">
    <div class="poster__backdrop" role="img" aria-label="Abstract bokeh background of soft glowing circles in yellow, green, cyan and deep blue"></div>
    <blockquote class="quote">
      <span class="quote__line">"we walk not</span>
      <span class="quote__line">in order to arrive</span>
      <span class="quote__line">at the promise land</span>
      <span class="quote__line">but because</span>
      <span class="quote__line">walking itself is</span>
      <span class="quote__line">a revolution"</span>
    </blockquote>
    <p class="author">Peter Ambrick</p>
  </main>
</body>
</html>
```